Propose a revamped landing page

One template we like eg is https://www.trovask.com but but cluttered Our logo and colors are attached to our logo and colors are printed on a white background what we have. So font usage ...
1 page

```html
<!DOCTYPE html>
<html lang="en">
<head>
<meta charset="utf-8">
<title>Voltwise – Always switch to the cheapest energy</title>
<link href="https://fonts.googleapis.com/css2?family=Montserrat:wght@400;600;700;800&family=Open+Sans:wght@400;600;700&display=swap" rel="stylesheet">
<style>
:root{
  --orange:#f8a51b;
  --orange-deep:#f26a21;
  --ink:#1f1f1f;
  --muted:#555;
  --paper:#f4f4f7;
  --white:#fff;
  --dark:#2b2b2b;
  --darker:#1e1e1e;
  --slate:#3c3c3c;
  --teal:#14a79b;
}
*{box-sizing:border-box;margin:0;padding:0}
html,body{width:1200px;height:3913px;overflow:hidden}
body{font-family:"Open Sans",Arial,sans-serif;color:var(--ink);background:var(--paper);position:relative}
.abs{position:absolute}
h1,h2,h3{font-family:"Montserrat",Arial,sans-serif}

/* header */
.brand{left:28px;top:40px;font-family:"Montserrat",Arial,sans-serif;font-weight:800;font-size:30px;line-height:1;color:var(--ink);display:flex;align-items:center;gap:8px}
.brand .dot{width:14px;height:14px;border-radius:50%;background:var(--orange)}
.nav{right:40px;top:28px;display:flex;gap:26px;align-items:center;font-family:"Montserrat",Arial,sans-serif;font-weight:700;font-size:13px;z-index:3}
.nav .social{width:24px;height:24px;background:var(--ink);border-radius:3px}

.hero-title{left:28px;top:140px;width:600px;font-size:44px;line-height:1.12;font-weight:800}
.hero-text{left:28px;top:326px;width:600px;font-size:15px;line-height:1.6;color:var(--muted)}
.btn{display:inline-block;background:var(--orange-deep);color:var(--white);font-family:"Montserrat",Arial,sans-serif;font-weight:600;font-size:15px;border-radius:24px;padding:12px 36px}
.hero-btn{left:28px;top:430px}
.hero-art{left:640px;top:80px;width:460px;height:590px;border-radius:40px;background:linear-gradient(160deg,#e9e3d6,#c9a56a 60%,#7a5a30)}

/* features */
.section-title{font-size:30px;font-weight:800;line-height:1.25}
.features-title{left:78px;top:765px;width:560px}
.feature{top:935px;width:330px;height:230px;background:var(--white);border-radius:10px;box-shadow:0 8px 22px rgba(0,0,0,.14);padding:70px 24px 0;font-size:14px;line-height:1.6;color:var(--muted)}
.feature svg{position:absolute;left:24px;top:-30px}

/* prices */
.prices-title{left:0;width:1200px;top:1352px;text-align:center}
.prices-sub{left:0;width:1200px;top:1410px;text-align:center;font-size:17px;color:var(--ink)}
.price-card{top:1475px;width:185px;height:205px;background:var(--white);border-radius:8px;box-shadow:0 8px 22px rgba(0,0,0,.18);padding:10px}
.price-inner{border:1px solid #cfcfcf;border-radius:5px;height:100%;display:flex;flex-direction:column;justify-content:space-around;align-items:center;text-align:center;font-size:14px}
.price-inner hr{width:80%;border:0;border-top:1px solid #d8d8d8}
.price-inner .amount{font-family:"Montserrat",Arial,sans-serif;font-size:22px;font-weight:700;color:var(--orange-deep)}
.price-inner .amount small{font-size:12px;color:var(--ink);font-weight:400}
.price-inner.note{font-family:"Montserrat",Arial,sans-serif;font-weight:700;font-size:17px;line-height:1.35;padding:0 8px}
.price-foot{left:240px;width:720px;top:1740px;text-align:center;font-size:13px;line-height:1.55;color:var(--ink)}

/* steps */
.steps-title{left:0;width:1200px;top:1955px;text-align:center}

/* register */
.reg-art{left:60px;top:2580px;width:600px;height:500px;border-radius:40px;background:linear-gradient(135deg,#3a2a1a,#7b5a34 55%,#f3c76f)}
.reg-box{left:712px;top:2700px;width:460px}
.reg-box h2{font-size:27px;font-weight:800;margin-bottom:26px;white-space:nowrap}
.reg-box h3{font-size:18px;font-weight:700;margin-top:14px}
.reg-box p{font-size:14px;line-height:1.5;margin-top:6px}
.reg-link{display:block;margin-top:30px;font-family:"Montserrat",Arial,sans-serif;font-size:19px}

/* press */
.press-title{left:0;width:1200px;top:3215px;text-align:center}
.press-row{left:95px;width:1010px;display:flex;justify-content:space-between;align-items:center;font-family:"Montserrat",Arial,sans-serif;font-weight:700;font-size:24px;color:#7a7a7a}
.press-badge{width:46px;height:46px;border-radius:50%;background:#9a9a9a}

/* band */
.ask-band{left:0;top:3485px;width:1200px;height:105px;background:var(--teal);display:flex;align-items:center;justify-content:center;font-size:18px;color:var(--white)}
.ask-band b{color:var(--orange);font-weight:600}

/* footer */
.footer{left:0;top:3590px;width:1200px;height:283px;background:var(--dark);color:#e5e5e5;font-size:13px}
.footer .col{position:absolute;top:30px}
.footer h4{font-family:"Montserrat",Arial,sans-serif;font-size:16px;font-weight:700;color:var(--white);margin-bottom:14px}
.footer li{list-style:none;line-height:1.65}
.footer input{display:block;width:260px;height:34px;margin:16px 0 10px;background:#3a3a3a;border:0;color:#bbb;padding:0 10px;font:13px "Open Sans",Arial,sans-serif}
.footer .sub{width:270px;height:34px;background:var(--orange);border:0;font:600 14px "Montserrat",Arial,sans-serif;color:var(--ink)}
.footer .map{width:230px;height:150px;background:linear-gradient(135deg,#e9ece6,#cfd7cc)}
.footer .social-sq{width:32px;height:32px;background:#3b5998;border-radius:3px;margin-left:30px}
.copyright{left:0;top:3873px;width:1200px;height:40px;background:var(--darker);color:#aaa;font-size:12px;display:flex;align-items:center;padding-left:18px}
</style>
</head>
<body>

<!-- hero -->
<svg class="abs" style="left:0;top:0" width="1200" height="720" aria-hidden="true">
  <path d="M0,560 C300,660 700,700 1200,420 L1200,720 L0,720 Z" fill="var(--orange)"/>
  <path d="M0,610 C400,740 800,720 1200,560 L1200,720 L0,720 Z" fill="var(--paper)"/>
</svg>
<div class="abs hero-art" role="img" aria-label="Eagle landing on wooden signpost reading Choose, Upload, Recline, with power pylons behind"></div>
<div class="abs brand">Voltwise<span class="dot"></span></div>
<nav class="abs nav"><span>That's How it Works</span><span>Prices</span><span>Ask?</span><span>About Us</span><span>Operations</span><span>Experience</span><span>Press</span><span class="social"></span></nav>
<h1 class="abs hero-title">Always automatically switch to the cheapest energy</h1>
<p class="abs hero-text">The overwhelming majority of Austrians remain with the same energy provider year after year. And that, without knowing if they really get the best price. In all likelihood, you too are part of it.</p>
<a class="abs btn hero-btn">Register Now</a>

<!-- features -->
<h2 class="abs section-title features-title">Never pay too much for electricity &amp; gas again</h2>
<div class="abs feature" style="left:75px">
  <svg width="56" height="56" viewBox="0 0 56 56"><rect x="10" y="6" width="36" height="44" rx="3" fill="#fff" stroke="var(--orange-deep)" stroke-width="4"/><path d="M18 18h20M18 27h20M18 36h14" stroke="var(--ink)" stroke-width="3"/></svg>
  Gone are the days of bad deals, tedious rate comparison and boring exchange forms.
</div>
<div class="abs feature" style="left:435px">
  <svg width="56" height="56" viewBox="0 0 56 56"><path d="M30 6L16 30h12l-4 20 16-26H28z" fill="none" stroke="var(--orange-deep)" stroke-width="4" stroke-linejoin="round"/></svg>
  With the automatic change service for Voltwise recruits you will never again pay too much for electricity and gas. And that, without lifting a finger. We fight for you through the tariff jungle.
</div>
<div class="abs feature" style="left:795px">
  <svg width="56" height="56" viewBox="0 0 56 56"><text x="10" y="46" font-family="Montserrat,Arial,sans-serif" font-size="46" font-weight="800" fill="var(--orange-deep)">€</text></svg>
  So save your hard-earned money and become a Voltwise hero.
</div>

<!-- prices -->
<svg class="abs" style="left:0;top:1190px" width="1200" height="700" aria-hidden="true">
  <path d="M0,40 C400,0 800,0 1200,30 L1200,640 C800,700 400,700 0,660 Z" fill="var(--orange)"/>
</svg>
<h2 class="abs section-title prices-title">The cheapest of all super powers</h2>
<p class="abs prices-sub">From 24 euros you are there</p>
<div class="abs price-card" style="left:200px"><div class="price-inner"><span>Electricity / Gas</span><hr><span>1 meter</span><hr><span class="amount">24 € <small>/ year</small></span></div></div>
<div class="abs price-card" style="left:415px"><div class="price-inner"><span>Electricity &amp; Gas</span><hr><span>2 Counters</span><hr><span class="amount">36 € <small>/ year</small></span></div></div>
<div class="abs price-card" style="left:630px"><div class="price-inner note">The first fee will be charged only after your first change</div></div>
<div class="abs price-card" style="left:845px"><div class="price-inner"><span>Electricity &amp; Gas</span><hr><span>Save</span><hr><span class="amount">850 € <small>/ year</small></span><hr><span>At First Change</span></div></div>
<p class="abs price-foot">* Annual saving of an average Austrian household (3,500 kWh of electricity and 15,000 kWh of gas consumption) in the region with the greatest savings potential after the first change from the most widely used tariff of the local electricity and gas provider to the cheapest available provider according to the PowerWatch price monitor of 6.11.2018</p>

<!-- steps -->
<h2 class="abs section-title steps-title">How do I become Voltwise?</h2>
<svg class="abs" style="left:0;top:2040px" width="1200" height="470" viewBox="0 0 1200 470" font-family="Montserrat,Arial,sans-serif">
  <path d="M520,140 C600,150 650,160 670,165" stroke="#bdbdbd" stroke-width="16" fill="none"/>
  <path d="M650,265 C620,290 560,300 525,305" stroke="#bdbdbd" stroke-width="16" fill="none"/>
  <rect x="465" y="45" width="420" height="90" rx="45" fill="var(--orange)"/>
  <text x="560" y="82" font-size="19" font-weight="600" fill="var(--ink)">Once Login</text>
  <text x="560" y="108" font-size="11" fill="#333">Upload financial statements. Select preferences.</text>
  <text x="560" y="123" font-size="11" fill="#333">Finish the registration.</text>
  <rect x="290" y="175" width="405" height="85" rx="42" fill="var(--slate)"/>
  <text x="325" y="208" font-size="19" font-weight="600" fill="#fff">Automatic</text>
  <text x="325" y="230" font-size="11" fill="#eee">Pure change: We pick the cheapest fare for you</text>
  <text x="325" y="245" font-size="11" fill="#eee">and carry out the change automatically</text>
  <rect x="465" y="310" width="430" height="85" rx="42" fill="var(--orange-deep)"/>
  <text x="560" y="350" font-size="19" font-weight="600" fill="#fff">Sit Back and Save Money</text>
  <text x="560" y="374" font-size="11" fill="#fff">Always switch automatically to the low fare</text>
  <circle cx="465" cy="90" r="66" fill="#fff" stroke="var(--orange)" stroke-width="14"/>
  <text x="465" y="78" font-size="12" text-anchor="middle" fill="#333">STEP</text>
  <text x="465" y="112" font-size="34" text-anchor="middle" fill="var(--ink)">01</text>
  <circle cx="700" cy="218" r="58" fill="#fff" stroke="var(--slate)" stroke-width="14"/>
  <text x="700" y="206" font-size="12" text-anchor="middle" fill="#333">STEP</text>
  <text x="700" y="240" font-size="34" text-anchor="middle" fill="var(--ink)">02</text>
  <circle cx="465" cy="352" r="66" fill="#fff" stroke="var(--orange-deep)" stroke-width="14"/>
  <text x="465" y="340" font-size="12" text-anchor="middle" fill="#333">STEP</text>
  <text x="465" y="374" font-size="34" text-anchor="middle" fill="var(--ink)">03</text>
</svg>

<!-- register -->
<svg class="abs" style="left:0;top:2545px" width="1200" height="640" aria-hidden="true">
  <path d="M0,20 C400,0 800,0 1200,20 L1200,600 C800,540 400,560 0,620 Z" fill="var(--orange)"/>
</svg>
<div class="abs reg-art" role="img" aria-label="Eagle in flight with wings spread"></div>
<div class="abs reg-box">
  <h2>Register Once, Always Save</h2>
  <h3>Independently</h3>
  <p>We work only for you. In order to remain independent, we consciously do without commission deals with energy providers</p>
  <h3>Automatically</h3>
  <p>You sign up once and we'll do the rest. All automatically.</p>
  <h3>Fair</h3>
  <p>Voltwise stays more in 98 rest. Despite service change.</p>
  <a class="reg-link">Register Now ⟶</a>
</div>

<!-- press -->
<h2 class="abs section-title press-title">Known From</h2>
<div class="abs press-row" style="top:3290px"><span class="press-badge"></span><span>startkiste</span><span>bytewelle</span><span>Talbote Nord</span><span>Der Morgenruf</span></div>
<div class="abs press-row" style="top:3350px"><span>Die Feder</span><span>KORSO</span><span>WELLE 47</span><span>Zeitkreis</span><span>kapitalo.</span></div>

<div class="abs ask-band"><span>Questions? Read <b>Ask?</b> for a quick answer</span></div>

<!-- footer -->
<footer class="abs footer">
  <div class="col" style="left:28px"><h4>Company</h4><ul><li>What is Voltwise?</li><li>About Us</li><li>How It Works?</li><li>Conditions</li><li>Data Protection</li><li>Ask?</li><li>Contact Us</li></ul></div>
  <div class="col" style="left:222px"><h4>Switch Energy</h4><ul><li>Switch Electricity</li><li>Switch Gas</li></ul></div>
  <div class="col" style="left:415px"><h4>Newsletter</h4><p>Subscribe to our newsletter for latest updates</p><input value="Email..." aria-label="Email"><button class="sub">Subscribe</button></div>
  <div class="col" style="left:712px"><h4>Locate Us</h4><div class="map" role="img" aria-label="Map showing office location"></div></div>
  <div class="col" style="left:1000px"><h4>Connect With Us</h4><div class="social-sq"></div></div>
</footer>
<div class="abs copyright">© Copyright All Voltwise</div>

</body>
</html>
```